Web design for software company

I'm a software developer that designs high end specialist web applications, mobile apps and user friendly applications for medium to large customers. I integrate different systems together within a company and provide web based applications or mobile apps to view and edit information in that web of linked systems.

I currently work alone, basically selling my time on specialist projects, but also build my own software solutions which I eventually want to put into the market.

My company name is Overthread (lowercase 'L' for logic) and I work from the Netherlands. I've attached my current logo which is basically just text in VOXbox font. Current colours are mustard yellow and grey, but i'm open to other options to better fit the web design.

I've got a sort of slogan: "Specialized software development" - better ideas are welcome. The slogan in the logo attachment is older.

I'm looking for a site design that reflects my work as being on the cutting edge of technology, but being clear and simple. My thinking with the name Overthread is that it refers to the underlying mechanism and logic of software.

The site will not be text heavy, so some kind of large graphic to do with software design is welcome. I expect about 4 or 5 main pages or sections of the site in which i'll eventually add things like a blog or contact info etc.

Industry/Entity Type

It Company

Number of Pages Required

1 page

Font styles to use
Sans Serif

Requirements
Nice to have
• A large graphic or photo relevant to my focus as a software developer. Something that shows connecting of software systems with perhaps a variety of devices/browsers that would display data from that cloud of systems.
• Something like these (allthough these are ugly - but the idea is what i mean):
• http://img4.pixvaultimages.example/2000517/22458/i/450/pixvault_224581133-Cloud-computing-user-interface.jpg
• http://business.tamblinet.example/images/modules/mobile-device-policy-design-banner.png
• https://www.pagecraftly.example/images/responsive-web-design.jpg
• http://www.norvexa.example/images/web_apps.png
• https://www.keyportal.example/assets/img/product/web-app@2x.png?v2
Should not have
• Photographs of smiling happy people looking at a screen that make it look like it's a huge business with many offices. I'm a one-man company which could perhaps grow a little bit, but i want to focus on my expertise instead of size.

```html
<!DOCTYPE html>
<html lang="en">
<head>
<meta charset="utf-8">
<title>Overthread — Specialized Software Development</title>
<link href="https://fonts.googleapis.com/css2?family=Orbitron:wght@700;800;900&family=Lato:wght@400;700&family=Cinzel:wght@400;700&display=swap" rel="stylesheet">
<style>
:root{
  --blue:#0a57cc;
  --blue-dark:#0840a0;
  --orange:#c2460f;
  --ink:#141414;
  --text:#222;
  --rule:#d6d6d6;
  --footer:#121416;
  --footer-bar:#2b2d30;
  --footer-text:#e6e6e6;
  --hero-a:#1b2432;
  --hero-b:#55657a;
}
*{box-sizing:border-box;margin:0;padding:0}
html,body{width:1200px;height:2219px;overflow:hidden;background:#fff}
body{position:relative;font-family:'Lato',sans-serif;color:var(--text)}
.abs{position:absolute}

/* header */
.topline{left:0;top:0;width:1200px;height:4px;background:#555}
.header{left:0;top:4px;width:1200px;height:97px;background:linear-gradient(#fff,#f1f1f1)}
.brand{left:100px;top:30px;display:flex;align-items:center;gap:12px}
.brand-mark{width:48px;height:48px;border-radius:50%;background:var(--blue)}
.brand-name{font-family:'Orbitron',sans-serif;font-weight:900;font-size:30px;color:var(--blue);letter-spacing:1px}
.contact-bar{right:100px;top:16px;display:flex;gap:22px;font-size:15px;font-weight:700;color:var(--ink);align-items:center}
.contact-bar span{display:flex;align-items:center;gap:8px}
.nav{left:505px;top:66px;display:flex;font-size:18px;font-weight:700;color:var(--ink)}
.nav a{color:inherit;text-decoration:none;padding:0 20px;border-left:1px solid #ccc;line-height:24px}
.nav a:first-child{border-left:none;color:var(--blue);font-weight:400}

/* hero */
.hero{left:0;top:101px;width:1200px;height:515px;background:radial-gradient(ellipse at 75% 40%,#6f8196 0%,var(--hero-b) 30%,var(--hero-a) 85%)}
.hero-title{left:102px;top:315px;font-family:'Lato',sans-serif;font-weight:700;font-size:36px;line-height:44px;color:#fff;letter-spacing:1px}
.hero-arrow{top:342px;width:24px;height:28px;background:rgba(200,200,200,.6);display:flex;align-items:center;justify-content:center}
.hero-shadow{left:200px;top:616px;width:800px;height:22px;background:radial-gradient(ellipse at 50% 0%,rgba(0,0,0,.28),transparent 70%)}

/* about */
.section-title{font-family:'Orbitron',sans-serif;font-weight:800;font-size:36px;color:var(--ink);letter-spacing:1px}
.section-title em{font-style:normal;color:var(--blue)}
.about-title{left:100px;top:712px}
.about-rule{left:99px;top:779px;width:656px;height:1px;background:var(--rule)}
.about-text{left:99px;top:796px;width:660px;font-size:13.5px;line-height:24.5px;color:#222}
.btn-outline{display:inline-block;border:2px solid var(--blue);color:var(--ink);font-size:15px;text-align:center}
.about-btn{left:98px;top:933px;width:112px;height:34px;line-height:30px}
.about-photo{left:799px;top:636px;width:290px;height:438px;background:linear-gradient(#e8eef5,#b9c8da 60%,#8da3c0)}

/* services */
.service{top:1074px;width:400px;height:407px;color:#fff;text-align:center}
.service.blue{background:linear-gradient(135deg,#0b4fc0,#0a3d98 60%,#0d56c6)}
.service.orange{background:linear-gradient(135deg,#a83a0c,#c8500f 55%,#b8400c)}
.service-icon{position:absolute;left:151px;top:65px;width:98px;height:98px;border-radius:50%;background:#fff;display:flex;align-items:center;justify-content:center}
.service-name{position:absolute;left:0;top:172px;width:100%;font-size:25px;font-weight:700}
.service-text{position:absolute;left:90px;top:214px;width:220px;font-size:13.3px;font-weight:700;line-height:22px}
.service-btn{position:absolute;left:152px;top:310px;width:96px;height:30px;border:2px solid #fff;font-size:14.5px;font-weight:700;line-height:26px}

/* testimonials & why */
.col-divider{left:596px;top:1481px;width:10px;height:391px;background:linear-gradient(90deg,transparent,rgba(0,0,0,.08),transparent)}
.sub-title{font-family:'Orbitron',sans-serif;font-weight:800;font-size:27px;color:var(--ink);letter-spacing:.5px}
.sub-title em{font-style:normal;color:var(--blue)}
.testi-title{left:97px;top:1532px}
.why-title{left:630px;top:1532px}
.testi-rule{left:99px;top:1587px;width:468px;height:1px;background:var(--rule)}
.why-rule{left:627px;top:1587px;width:468px;height:1px;background:var(--rule)}
.avatar{left:99px;top:1613px;width:128px;height:128px;border-radius:50%;border:3px solid #9bb9e6;background:linear-gradient(#dfe7f2,#a9bcd6)}
.quote-mark{left:252px;top:1600px;font-family:Georgia,serif;font-size:50px;color:#bbb;line-height:1}
.quote-text{left:254px;top:1613px;width:314px;font-size:14.5px;line-height:24px;text-align:justify;color:#222;text-indent:24px}
.quote-name{left:252px;top:1776px;font-family:'Cinzel',serif;font-size:17px;color:var(--blue)}
.quote-org{left:252px;top:1799px;font-size:13px;color:#222}
.why-item{left:627px;width:468px;display:flex;gap:20px}
.why-icon{width:34px;flex:none;padding-top:4px}
.why-head{font-family:'Cinzel',serif;font-size:16.5px;color:var(--ink);line-height:20px}
.why-body{font-size:13.5px;line-height:18px;color:#222}
.why-sep{left:680px;width:415px;height:1px;background:#e2e2e2}

/* footer */
.footer{left:0;top:1872px;width:1200px;height:305px;background:var(--footer)}
.footer-head{font-family:'Orbitron',sans-serif;font-weight:800;font-size:17px;color:#fff;letter-spacing:1px}
.footer-head em{font-style:normal;color:var(--blue)}
.footer-rule{height:1px;background:#2a2c2f}
.quick-links{left:80px;top:1970px;list-style:none;font-size:13.5px;color:var(--footer-text)}
.quick-links li{height:30px;line-height:20px;padding-left:18px;position:relative}
.quick-links li::before{content:"";position:absolute;left:0;top:8px;width:4px;height:4px;border-radius:50%;background:var(--blue)}
.contact-detail{left:302px;top:1970px;font-size:13.5px;color:var(--footer-text);line-height:18px}
.contact-detail .line{display:flex;align-items:center;gap:10px}
.form-field{left:617px;width:258px;height:34px;background:#fff;border-radius:2px;font-size:12.5px;color:#888;padding:9px 10px}
.form-submit{left:617px;top:2098px;width:120px;height:34px;background:var(--blue);color:#fff;font-size:17px;font-weight:700;text-align:center;line-height:34px;border-radius:2px}
.follow{left:968px;display:flex;align-items:center;gap:10px;font-size:12.5px;font-weight:700;color:#fff}
.follow i{width:32px;height:32px;border-radius:50%;display:block}
.copyright{left:0;top:2177px;width:1200px;height:42px;background:var(--footer-bar);color:#fff;font-size:13px;font-weight:700;text-align:center;line-height:42px}
</style>
</head>
<body>

<div class="abs topline"></div>
<header class="abs header">
  <div class="abs brand" style="top:26px"><span class="brand-mark"></span><span class="brand-name">OVERTHREAD</span></div>
  <div class="abs contact-bar">
    <span><svg width="16" height="16" viewBox="0 0 24 24"><path fill="#0a57cc" d="M6.6 10.8a15 15 0 0 0 6.6 6.6l2.2-2.2c.3-.3.7-.4 1-.2 1.1.4 2.3.6 3.6.6.6 0 1 .4 1 1V20c0 .6-.4 1-1 1A17 17 0 0 1 3 4c0-.6.4-1 1-1h3.5c.6 0 1 .4 1 1 0 1.3.2 2.5.6 3.6.1.3 0 .7-.2 1z"/></svg>(123) 456 7890</span>
    <span><svg width="16" height="12" viewBox="0 0 16 12"><rect width="16" height="12" fill="#0a57cc"/><path d="M0 0l8 6 8-6" stroke="#fff" fill="none" stroke-width="1.4"/></svg><span style="font-weight:400">info@overthread.com</span></span>
  </div>
  <nav class="abs nav">
    <a href="#">Home</a><a href="#">Services</a><a href="#">About Me</a><a href="#">Software Solutions</a><a href="#">Contact Us</a>
  </nav>
</header>

<section class="abs hero" role="img" aria-label="Hand touching a glowing network of connected devices, servers and database technology labels"></section>
<h1 class="abs hero-title">SPECIALIZED SOFTWARE<br>DEVELOPMENT</h1>
<div class="abs hero-arrow" style="left:0"><svg width="10" height="12" viewBox="0 0 10 12"><path d="M8 1L2 6l6 5" stroke="#333" stroke-width="2" fill="none"/></svg></div>
<div class="abs hero-arrow" style="left:1176px"><svg width="10" height="12" viewBox="0 0 10 12"><path d="M2 1l6 5-6 5" stroke="#333" stroke-width="2" fill="none"/></svg></div>
<div class="abs hero-shadow"></div>

<h2 class="abs section-title about-title">ABOUT <em>ME</em></h2>
<div class="abs about-rule"></div>
<p class="abs about-text">Myself am a software developer that designs high end specialist web applications, mobile apps and user friendly applications for medium to large customers. I integrate different systems together within a company and provide web based applications or mobile apps to view and edit information in that web of linked systems. I currently work alone, basically selling my time on specialist projects, but also build my own software solutions which I eventually want to put into the market.</p>
<a class="abs btn-outline about-btn">Read More</a>
<div class="abs about-photo" role="img" aria-label="Portrait of the developer in shirt and tie with arms crossed"></div>

<section class="abs service blue" style="left:0">
  <div class="service-icon"><svg width="64" height="64" viewBox="0 0 64 64" fill="none" stroke="#c2460f" stroke-width="3.5"><circle cx="32" cy="32" r="26"/><ellipse cx="32" cy="32" rx="11" ry="26"/><path d="M8 22h48M8 42h48"/></svg></div>
  <h3 class="service-name">Web Applications</h3>
  <p class="service-text">Lorem ipsum dolor sit amet, consectetuer adipiscing elit, seddiam nonummy nibh euismod tincidunt ut laoreetfgf doloremagna</p>
  <a class="service-btn">Read More</a>
</section>
<section class="abs service orange" style="left:400px">
  <div class="service-icon"><svg width="56" height="60" viewBox="0 0 56 60"><rect x="14" y="6" width="24" height="46" rx="3" fill="none" stroke="#0a57cc" stroke-width="4"/><rect x="19" y="13" width="14" height="28" fill="#0a57cc"/><rect x="40" y="6" width="5" height="5" fill="#0a57cc"/><rect x="46" y="12" width="5" height="5" fill="#0a57cc"/><rect x="41" y="19" width="5" height="5" fill="#0a57cc"/></svg></div>
  <h3 class="service-name">Mobile Applications</h3>
  <p class="service-text">Lorem ipsum dolor sit amet, consectetuer adipiscing elit, seddiam nonummy nibh euismod tincidunt ut laoreetfgf doloremagna</p>
  <a class="service-btn">Read More</a>
</section>
<section class="abs service blue" style="left:800px">
  <div class="service-icon"><svg width="66" height="50" viewBox="0 0 66 50"><path d="M16 44a12 12 0 0 1-1-24 17 17 0 0 1 32-4 13 13 0 0 1 4 28z" fill="#c2460f"/><circle cx="33" cy="30" r="8" fill="none" stroke="#fff" stroke-width="4" stroke-dasharray="4 2.3"/><circle cx="33" cy="30" r="3" fill="#fff"/></svg></div>
  <h3 class="service-name">Software Solutions</h3>
  <p class="service-text">Lorem ipsum dolor sit amet, consectetuer adipiscing elit, seddiam nonummy nibh euismod tincidunt ut laoreetfgf doloremagna</p>
  <a class="service-btn">Read More</a>
</section>

<div class="abs col-divider"></div>
<h2 class="abs sub-title testi-title">CLIENT <em>TESTIMONIALS</em></h2>
<div class="abs testi-rule"></div>
<div class="abs avatar" role="img" aria-label="Client portrait"></div>
<div class="abs quote-mark">"</div>
<p class="abs quote-text">Lorem ipsum dolor sit amet, consectetuer adipiscing elit, sed diam nonummy nibh euismod tincidunt ut laoreet dolore magna aliquam erat volutpat. Ut wisi enim ad minim veniam, quis nostrud exerci tation ullamcorper suscipit lobortis nisl ut aliquip.</p>
<div class="abs quote-name">Lena Vosberg</div>
<div class="abs quote-org">Kestrel Guard Systems</div>

<h2 class="abs sub-title why-title">WHY <em>CHOOSE ME</em></h2>
<div class="abs why-rule"></div>
<div class="abs why-item" style="top:1612px">
  <div class="why-icon"><svg width="30" height="30" viewBox="0 0 30 30"><rect x="1" y="1" width="28" height="28" fill="#0a57cc"/><circle cx="15" cy="15" r="9" fill="none" stroke="#fff" stroke-width="2"/><circle cx="15" cy="15" r="4" fill="#fff"/></svg></div>
  <div><div class="why-head">My Track record</div><div class="why-body">Lorem ipsum dolor sit amet, consectetuer adipiscing elit, sed diam nonummy nibh euismod tincidunt ut laoreet.</div></div>
</div>
<div class="abs why-sep" style="top:1677px"></div>
<div class="abs why-item" style="top:1686px">
  <div class="why-icon"><svg width="30" height="32" viewBox="0 0 30 32"><path d="M15 2a12 12 0 0 0-9 20v8h12v-4h5l1-6 4-1-3-6A12 12 0 0 0 15 2z" fill="#0a57cc"/><circle cx="14" cy="13" r="5" fill="none" stroke="#fff" stroke-width="2.5" stroke-dasharray="3 2"/></svg></div>
  <div><div class="why-head">My wide range of experience</div><div class="why-body">Lorem ipsum dolor sit amet, consectetuer adipiscing elit, sed diam nonummy nibh euismod tincidunt ut laoreet.</div></div>
</div>
<div class="abs why-sep" style="top:1751px"></div>
<div class="abs why-item" style="top:1760px">
  <div class="why-icon"><svg width="34" height="34" viewBox="0 0 34 34"><rect x="10" y="1" width="8" height="4" fill="#0a57cc"/><circle cx="14" cy="19" r="12" fill="none" stroke="#0a57cc" stroke-width="4"/><path d="M14 12v7h5" stroke="#0a57cc" stroke-width="3" fill="none"/><circle cx="27" cy="27" r="6" fill="#0a57cc"/></svg></div>
  <div><div class="why-head">Great project execution-We will deliver</div><div class="why-body">Lorem ipsum dolor sit amet, consectetuer adipiscing elit, sed diam nonummy nibh euismod tincidunt ut laoreet.</div></div>
</div>

<footer class="abs footer"></footer>
<div class="abs footer-head" style="left:80px;top:1922px">QUICK <em>LINKS</em></div>
<div class="abs footer-head" style="left:302px;top:1922px">CONTACT <em>DETAIL</em></div>
<div class="abs footer-head" style="left:617px;top:1922px">QUICK <em>CONTACT</em></div>
<div class="abs footer-head" style="left:968px;top:1922px">FOLLOW <em>US</em></div>
<div class="abs footer-rule" style="left:80px;top:1956px;width:180px"></div>
<div class="abs footer-rule" style="left:302px;top:1956px;width:260px"></div>
<div class="abs footer-rule" style="left:617px;top:1956px;width:258px"></div>
<div class="abs footer-rule" style="left:968px;top:1956px;width:150px"></div>

<ul class="abs quick-links">
  <li>Home</li><li>Services</li><li>About Me</li><li>Software Solutions</li><li>Contact Us</li>
</ul>

<div class="abs contact-detail">
  <div style="font-weight:700;font-size:15px">OVERTHREAD</div>
  <div style="margin-top:4px">123, Ut wisi enim ad minim veniam,<br>Mor nostrni tation -123 456</div>
  <div class="line" style="margin-top:18px"><svg width="13" height="13" viewBox="0 0 24 24"><path fill="#0a57cc" d="M6.6 10.8a15 15 0 0 0 6.6 6.6l2.2-2.2c.3-.3.7-.4 1-.2 1.1.4 2.3.6 3.6.6.6 0 1 .4 1 1V20c0 .6-.4 1-1 1A17 17 0 0 1 3 4c0-.6.4-1 1-1h3.5c.6 0 1 .4 1 1 0 1.3.2 2.5.6 3.6.1.3 0 .7-.2 1z"/></svg>(123) 456 7890</div>
  <div class="line" style="margin-top:16px"><svg width="14" height="13" viewBox="0 0 14 13"><rect x="3" y="0" width="8" height="4" fill="#0a57cc"/><rect x="0" y="4" width="14" height="6" fill="#0a57cc"/><rect x="3" y="8" width="8" height="5" fill="#0a57cc"/></svg>(123) 456 7890</div>
  <div class="line" style="margin-top:16px"><svg width="13" height="10" viewBox="0 0 16 12"><rect width="16" height="12" fill="#0a57cc"/><path d="M0 0l8 6 8-6" stroke="#fff" fill="none" stroke-width="1.4"/></svg>info@overthread.com</div>
</div>

<div class="abs form-field" style="top:1974px">Name</div>
<div class="abs form-field" style="top:2015px">Email</div>
<div class="abs form-field" style="top:2057px">Message</div>
<div class="abs form-submit">Submit</div>

<div class="abs follow" style="top:1974px"><i style="background:#1d4fa8"></i>FRIENDHUB</div>
<div class="abs follow" style="top:2016px"><i style="background:#1bb0df"></i>CHIRPLINE</div>
<div class="abs follow" style="top:2057px"><i style="background:#137bb8"></i>LINKWORK</div>
<div class="abs follow" style="top:2100px"><i style="background:#f39a1c"></i>RSS FEED</div>

<div class="abs copyright">Copyright © 2016 Overthread. All Rights Reserved.</div>

</body>
</html>
```